Landscaping Company Flyer Design Project

I need a flyer design for a landscaping company based in Mokena, Illinois called Brightfold Yard & Garden. These flyers will be distributed door to door throughout the community. I want a design that is simple to read and allows the eye to flow along through it, nothing crammed. My logo is attached and would be nice to have on there, sometimes I take the tree off the top of logo to use which you can do as well if preferred. I also attached some pictures which may or may not be used depending on what you think. Some important information I would like on there is: 815-342-9186, company name, BrtfldYard.com, free estimates. fully insured. I would also like to list some services on there such as: Landscape Design & Construction, Lawn Maintenance, Fertilization & Weed Control, Hardscape Construction, Bush Trimming, Aeration, Thatch Removal, Mulch & Rock Installation, New Lawn Installation, Clean-Ups, and more. A company slogan I like to use sometimes is Let Your Yard Find the Brightfold Touch. Also I like to write Dependable professionals dedicated to the quality of your property. One important thing I definitely want on there is either in the form of a coupon or just written somewhere where it will pop out is : Let us earn your business. Call now and get your first cut free of charge. I have a lot of different logo sizes and different formats such as vector or .pdf if needed, so let me know. Also I would like the flyer to be standard paper size 8.5X11

```html
<!DOCTYPE html>
<html lang="en">
<head>
<meta charset="utf-8">
<title>Brightfold Yard &amp; Garden Flyer</title>
<link href="https://fonts.googleapis.com/css2?family=Noto+Serif:wght@400;700&display=swap" rel="stylesheet">
<style>
  :root {
    --page-bg: #e9e6e1;
    --band-black: #0b0b0b;
    --brand-green: #6cbf2e;
    --bright-green: #8ccf3c;
    --deep-green: #1f5a2a;
    --ink: #111111;
    --paper: #ffffff;
  }
  * { box-sizing: border-box; margin: 0; padding: 0; }
  html, body {
    width: 1200px; height: 900px; overflow: hidden;
    background: var(--page-bg);
    font-family: "Noto Serif", "Times New Roman", serif;
  }
  .flyer {
    position: absolute; left: 257px; top: 40px;
    width: 638px; height: 826px;
    background: var(--paper);
    box-shadow: 0 6px 18px rgba(0,0,0,0.35);
    overflow: hidden;
  }
  .header {
    position: absolute; left: 0; top: 0; width: 100%; height: 120px;
    background: var(--band-black);
  }
  .brand {
    position: absolute; left: 30px; top: 36px;
    display: flex; align-items: center; gap: 10px;
  }
  .brand-mark { width: 22px; height: 22px; background: var(--brand-green); flex: none; }
  .brand-name {
    color: var(--brand-green); font-size: 19px; font-weight: 700; line-height: 23px;
    white-space: nowrap;
  }
  .contact {
    position: absolute; right: 32px; top: 30px; text-align: right;
    color: var(--bright-green); font-size: 19px; line-height: 25px;
  }
  .assurance {
    font-size: 13px; line-height: 20px; letter-spacing: 0.5px; color: var(--paper);
  }
  .rule {
    position: absolute; left: 0; width: 100%; height: 7px;
    background: linear-gradient(var(--bright-green), var(--brand-green));
  }
  .rule-top { top: 120px; }
  .rule-bottom { top: 742px; }
  .photo { position: absolute; }
  .photo-hero {
    left: 0; top: 127px; width: 638px; height: 300px;
    background: linear-gradient(180deg, #c2b196 0%, #9c8a70 38%, #5e8a34 58%, #6aa53a 78%, #4f8a2a 100%);
  }
  .photo-framed {
    border: 4px solid var(--brand-green);
    box-shadow: 0 3px 8px rgba(0,0,0,0.4);
  }
  .photo-left {
    left: -4px; top: 385px; width: 242px; height: 132px;
    background: linear-gradient(160deg, #6e9a4a, #4a7a30 60%, #8a9a3a 100%);
  }
  .photo-right {
    left: 400px; top: 385px; width: 242px; height: 130px;
    background: linear-gradient(200deg, #4c7a35, #6f8f50 55%, #9a957a 100%);
  }
  .photo-center {
    left: 198px; top: 425px; width: 240px; height: 138px;
    background: linear-gradient(180deg, #9a5a42 0%, #7d4a38 40%, #3f7a2a 70%, #5a9a34 100%);
  }
  .copy {
    position: absolute; left: 0; top: 576px; width: 100%; text-align: center;
  }
  .headline {
    color: var(--deep-green); font-size: 24px; font-weight: 700; line-height: 32px;
  }
  .tagline {
    color: var(--deep-green); font-size: 15px; font-weight: 700; line-height: 22px;
    margin-bottom: 8px;
  }
  .services { list-style: none; color: var(--ink); font-size: 16.5px; line-height: 22px; }
  .sep {
    display: inline-block; width: 2px; height: 12px; margin: 0 6px;
    background: var(--brand-green); vertical-align: 0;
  }
  .footer {
    position: absolute; left: 0; top: 749px; width: 100%; height: 77px;
    background: var(--band-black);
    display: flex; align-items: center; justify-content: center;
    color: var(--bright-green); font-size: 16.5px;
  }
</style>
</head>
<body>
  <main class="flyer">
    <header class="header">
      <div class="brand">
        <span class="brand-mark"></span>
        <span class="brand-name">Brightfold<br>Yard &amp; Garden</span>
      </div>
      <div class="contact">
        <p class="phone">Ph: 815-342-9186</p>
        <p class="web">www.BrtfldYard.com</p>
        <p class="assurance">Free Estimates &middot; Fully Insured</p>
      </div>
    </header>
    <div class="rule rule-top"></div>

    <div class="photo photo-hero" role="img" aria-label="Large home with manicured front lawn, curved walkway and shrub beds"></div>
    <div class="photo photo-framed photo-left" role="img" aria-label="Garden path lined with yellow lilies and greenery"></div>
    <div class="photo photo-framed photo-right" role="img" aria-label="Stone steps and retaining wall with flowering plants"></div>
    <div class="photo photo-framed photo-center" role="img" aria-label="Brick house with sculpted round hedges"></div>

    <section class="copy">
      <h1 class="headline">Let Your Yard Find the Brightfold Touch</h1>
      <p class="tagline">Dependable professionals dedicated to the quality of your property</p>
      <ul class="services">
        <li>Landscape Design &amp; Construction Lawn Maintenance</li>
        <li>Fertilization &amp; Weed Control<span class="sep"></span>Hardscape Construction<span class="sep"></span>Bush Trimming</li>
        <li>Aeration<span class="sep"></span>Thatch Removal<span class="sep"></span>Mulch &amp; Rock Installation</li>
        <li>New Lawn Installation<span class="sep"></span>Clean-Ups, and more</li>
      </ul>
    </section>

    <div class="rule rule-bottom"></div>
    <footer class="footer">
      <p>Let us earn your business. Call now and get your first cut free of charge.</p>
    </footer>
  </main>
</body>
</html>
```